Brisket Glazing

Modern glazing company specializing in commercial fit outs, pool fencing, frameless showers and glass splash backs, im after a very young/modern logo, it doesnt have to be revelent to glazing and a classy "boss like" design for the card. thank you in advanced
Updates

im thinking carbon fiber back ground or something along that line with bright orange wording or something maybe, open to suggestions 

Industry/Entity Type

Fencing

Contact Information for Business Card

company name, name, phone and products

```html
<!DOCTYPE html>
<html lang="en">
<head>
<meta charset="utf-8">
<title>Brisket Glazing – Business Card</title>
<link rel="stylesheet" href="https://fonts.googleapis.com/css2?family=Open+Sans:wght@400;600;700&family=Ubuntu:wght@500;700&display=swap">
<style>
  :root {
    --orange: #f05a28;
    --orange-faint: #f2774c;
    --charcoal: #2f2d2e;
    --white: #ffffff;
    --page: #e9e6e3;
  }
  * { box-sizing: border-box; margin: 0; padding: 0; }
  html, body { width: 1200px; height: 1000px; overflow: hidden; }
  body {
    position: relative;
    background: var(--page);
    font-family: "Open Sans", Arial, sans-serif;
  }

  .brand-mark {
    position: absolute;
    top: 70px; right: 40px;
    width: 300px;
    text-align: center;
    font-family: "Ubuntu", Arial, sans-serif;
    font-weight: 700;
    font-size: 30px;
    line-height: 1.1;
    color: var(--orange);
    text-transform: uppercase;
  }

  .card {
    position: absolute;
    width: 700px; height: 400px;
    overflow: hidden;
    box-shadow: 0 8px 22px rgba(0,0,0,.18);
  }

  /* Front */
  .card-front { left: 80px; top: 60px; background: var(--charcoal); }
  .card-front .edge-tab {
    position: absolute; width: 44px; background: var(--orange);
  }
  .card-front .edge-tab.left  { left: 0;  top: 60px; bottom: 14px; border-radius: 0 34px 34px 0; }
  .card-front .edge-tab.right { right: 0; top: 14px; bottom: 60px; border-radius: 34px 0 0 34px; }
  .card-front .company-name {
    position: absolute; left: 0; right: 0; top: 160px;
    text-align: center;
    font-family: "Ubuntu", Arial, sans-serif;
    font-weight: 700;
    font-size: 50px;
    color: var(--orange);
    text-transform: uppercase;
    letter-spacing: 1px;
  }

  /* Back */
  .card-back { left: 420px; top: 540px; background: var(--orange); }
  .card-back .edge-tab {
    position: absolute; left: 0; top: 40px; bottom: 14px; width: 48px;
    background: var(--charcoal);
    border-radius: 0 30px 30px 0;
  }
  .card-back .faint-name {
    position: absolute; left: 150px; top: 40px;
    font-family: "Ubuntu", Arial, sans-serif;
    font-weight: 700;
    font-size: 92px;
    line-height: 1;
    color: var(--orange-faint);
    text-transform: uppercase;
    white-space: nowrap;
  }
  .contact-block { position: absolute; left: 220px; top: 78px; color: var(--white); }
  .person-name {
    font-family: "Ubuntu", Arial, sans-serif;
    font-weight: 700; font-size: 26px; letter-spacing: 4px;
    text-transform: uppercase;
    margin-bottom: 18px;
  }
  .contact-row { display: flex; align-items: center; gap: 22px; height: 42px; font-size: 19px; }
  .contact-row svg { width: 30px; height: 30px; flex: none; }
  .specialty-heading {
    position: absolute; left: 230px; top: 272px;
    color: var(--white); font-size: 21px; text-transform: uppercase;
  }
  .specialty-band {
    position: absolute; left: 222px; right: 0; top: 306px; height: 80px;
    background: var(--charcoal);
    border-radius: 20px 0 0 20px;
    display: grid; grid-template-columns: 1fr 1fr;
    align-content: center; row-gap: 14px;
    padding: 0 18px;
    list-style: none;
    color: var(--white); font-size: 16px; text-transform: uppercase;
  }
</style>
</head>
<body>

  <div class="brand-mark">Brisket Glazing</div>

  <section class="card card-front">
    <div class="edge-tab left"></div>
    <div class="edge-tab right"></div>
    <div class="company-name">Brisket Glazing</div>
  </section>

  <section class="card card-back">
    <div class="edge-tab"></div>
    <div class="faint-name" aria-hidden="true">Brisket</div>

    <div class="contact-block">
      <div class="person-name">Dean Marlow</div>
      <div class="contact-row">
        <svg viewBox="0 0 30 30" aria-hidden="true"><rect x="8" y="2" width="14" height="26" rx="2" fill="none" stroke="#fff" stroke-width="2"/><line x1="8" y1="22" x2="22" y2="22" stroke="#fff" stroke-width="2"/><circle cx="15" cy="25" r="1.2" fill="#fff"/></svg>
        <span>0400 555 218</span>
      </div>
      <div class="contact-row">
        <svg viewBox="0 0 30 30" aria-hidden="true"><rect x="3" y="8" width="24" height="15" fill="#fff"/><polyline points="3,8 15,17 27,8" fill="none" stroke="#f05a28" stroke-width="1.6"/></svg>
        <span>dean@brisketglazing.com</span>
      </div>
      <div class="contact-row">
        <svg viewBox="0 0 30 30" aria-hidden="true"><circle cx="15" cy="15" r="13" fill="#fff"/><g fill="none" stroke="#f05a28" stroke-width="1.6"><ellipse cx="15" cy="15" rx="5.5" ry="13"/><line x1="2" y1="15" x2="28" y2="15"/><line x1="15" y1="2" x2="15" y2="28"/><line x1="4" y1="9" x2="26" y2="9"/><line x1="4" y1="21" x2="26" y2="21"/></g></svg>
        <span>www.brisketglazing.com</span>
      </div>
    </div>

    <div class="specialty-heading">Specializing in</div>
    <ul class="specialty-band">
      <li>Commercial fit outs</li>
      <li>Frameless showers</li>
      <li>Pool fencing</li>
      <li>Glass splash backs</li>
    </ul>
  </section>

</body>
</html>
```